A new presentation to our clients

we are a Real Estate agency, our website is www.dorelumia.com and it’s time to have a new, fashion and remarcable Business Card. we want to differentiate ourselves from other companies so we want a business card that differentiates us. we want the business card to impact our customers. in the competitive market that we have today, we have to be different and it is this difference that we seek

Target Market(s)

Real Estate Clients

Contact Information for Business Card

We search a totaly diferent card from the usual

Font styles to use
Sans Serif

Colors
e34197

Requirements
Must have
• Logo, adress, phone contact, e-mail, photo, and our website
Nice to have
• We would like to see a modern business card
Should not have
• Houses or building draws

```html
<!DOCTYPE html>
<html lang="en">
<head>
<meta charset="utf-8">
<title>Dore Lumia — Business Card</title>
<link rel="stylesheet" href="https://fonts.googleapis.com/css2?family=Lato:wght@400;700&display=swap">
<style>
  :root {
    --brand-pink: #e8145f;
    --card-white: #fbfbfa;
    --foil-silver: #dcdcdc;
    --ink-dark: #2a2a2a;
    --backdrop: #e9e9e7;
    --card-shadow: rgba(0, 0, 0, 0.18);
  }
  * { margin: 0; padding: 0; box-sizing: border-box; }
  html, body {
    width: 1200px;
    height: 1021px;
    overflow: hidden;
    background: var(--backdrop);
    font-family: "Lato", sans-serif;
  }
  .sheet {
    position: relative;
    width: 1200px;
    height: 1021px;
  }
  .card {
    position: absolute;
    width: 640px;
    height: 366px;
    box-shadow: 0 14px 30px var(--card-shadow);
  }
  .card--front {
    left: 120px;
    top: 90px;
    background: var(--brand-pink);
    display: flex;
    align-items: center;
    justify-content: center;
  }
  .card--back {
    left: 440px;
    top: 565px;
    background: var(--card-white);
    display: flex;
    flex-direction: column;
    align-items: center;
    justify-content: center;
  }
  .brand-name {
    font-weight: 700;
    letter-spacing: 1px;
    white-space: nowrap;
  }
  .card--front .brand-name {
    color: var(--foil-silver);
    font-size: 58px;
  }
  .card--back .brand-name {
    color: var(--brand-pink);
    font-size: 34px;
  }
  .rule {
    width: 60px;
    height: 2px;
    background: var(--brand-pink);
    margin: 22px 0;
  }
  .contact-list {
    list-style: none;
    display: flex;
    flex-wrap: wrap;
    justify-content: center;
    gap: 10px 22px;
    width: 500px;
    font-size: 14px;
    color: var(--ink-dark);
  }
  .contact-item {
    display: flex;
    align-items: center;
    gap: 6px;
  }
  .contact-icon {
    width: 12px;
    height: 12px;
    fill: var(--brand-pink);
  }
</style>
</head>
<body>
<main class="sheet">
  <section class="card card--front" aria-label="Card front">
    <span class="brand-name">Dore Lumia</span>
  </section>

  <section class="card card--back" aria-label="Card back">
    <span class="brand-name">Dore Lumia</span>
    <div class="rule"></div>
    <ul class="contact-list">
      <li class="contact-item">
        <svg class="contact-icon" viewBox="0 0 12 12"><path d="M6 0a4 4 0 0 0-4 4c0 3 4 8 4 8s4-5 4-8a4 4 0 0 0-4-4zm0 5.5A1.5 1.5 0 1 1 6 2.5a1.5 1.5 0 0 1 0 3z"/></svg>
        your address here
      </li>
      <li class="contact-item">
        <svg class="contact-icon" viewBox="0 0 12 12"><path d="M2.5 0.5l2 2.5-1.2 1.3a7 7 0 0 0 4.4 4.4L9 7.5l2.5 2-1.5 2C5 11.5 0.5 7 0.5 2z"/></svg>
        000 000 0000
      </li>
      <li class="contact-item">
        <svg class="contact-icon" viewBox="0 0 12 12"><path d="M0 2h12v1L6 7 0 3zM0 4.5l6 4 6-4V10H0z"/></svg>
        youremail@xyz.com
      </li>
      <li class="contact-item">
        <svg class="contact-icon" viewBox="0 0 12 12"><circle cx="6" cy="6" r="5.3" fill="none" stroke="#e8145f" stroke-width="1.2"/><path d="M0.7 6h10.6M6 0.7c-3 3-3 7.6 0 10.6M6 0.7c3 3 3 7.6 0 10.6" fill="none" stroke="#e8145f" stroke-width="1"/></svg>
        www.dorelumia.com
      </li>
    </ul>
    <div class="rule"></div>
  </section>
</main>
</body>
</html>
```